Quiet Verses Across Winter Evenings

Need a BOOK COVER, SPINE, and BACK for above named book. This is the story of my late wife (a university professor) told through her own songs and poems. It is about the people she loved, especially her grand children, her extensive professional and life interests, her family, friends, and festivities, her illness, etc.
Updates

Need extra days to review

Target Market(s)

Family and friends

Font styles to use
Other font styles liked:
• Times New Roman

Requirements
Must have
• Regret I haven't given much thought to it...
Nice to have
• Regret I haven't given much thought to it..
Should not have

```html
<!DOCTYPE html>
<html lang="en">
<head>
<meta charset="utf-8">
<title>Quiet Verses Across Winter Evenings – Cover Spread</title>
<link href="https://fonts.googleapis.com/css2?family=Tinos:wght@400;700&display=swap" rel="stylesheet">
<style>
  :root{
    --page:#ffffff;
    --sky-top:#7cc2ea;
    --sky-mid:#63a8d2;
    --sky-low:#4f8fc0;
    --cloud:#e9f2fa;
    --title-blue:#34479a;
    --silver:#9ea3a8;
    --ink:#0d1620;
    --white:#ffffff;
    --divider:rgba(255,255,255,0.55);
  }
  *{box-sizing:border-box;margin:0;padding:0}
  html,body{width:1200px;height:1200px;overflow:hidden;background:var(--page)}
  .spread{
    position:absolute;left:40px;top:180px;width:1120px;height:840px;
    background:linear-gradient(180deg,var(--sky-top) 0%,var(--sky-mid) 45%,var(--sky-low) 75%,var(--sky-mid) 100%);
    font-family:"Tinos","Times New Roman",serif;
    overflow:hidden;
  }
  .clouds{
    position:absolute;left:0;right:0;bottom:0;height:250px;
    background:linear-gradient(180deg,rgba(233,242,250,0) 0%,rgba(233,242,250,0.55) 55%,var(--cloud) 100%);
  }
  .panel{position:absolute;top:0;height:100%}
  .back{left:0;width:508px}
  .spine{left:508px;width:104px;border-left:1px solid var(--divider);border-right:1px solid var(--divider)}
  .front{left:612px;width:508px}

  .author-photo{
    position:absolute;left:154px;top:70px;width:199px;height:188px;
    border:3px solid var(--silver);
    background:linear-gradient(180deg,#f2ece8 0%,#b7735c 55%,#e6ddd7 100%);
  }
  .blurb{
    position:absolute;left:74px;top:274px;width:360px;text-align:center;
    color:var(--ink);font-size:12.5px;line-height:24.5px;
  }
  .blurb strong{font-weight:700}

  .book-title{
    position:absolute;text-align:center;
    color:var(--title-blue);font-weight:700;
  }
  .book-title span{display:block;white-space:nowrap}
  .book-title-front{left:30px;width:450px;top:196px;font-size:54px;line-height:64px}
  .book-title-back{left:120px;width:270px;top:585px;font-size:28px;line-height:34px}

  .front-author{
    position:absolute;left:0;right:0;top:140px;text-align:center;
    color:var(--white);font-weight:700;font-size:33px;letter-spacing:1px;
  }

  .spine-text{
    position:absolute;left:40px;white-space:nowrap;color:var(--title-blue);
    font-weight:700;font-size:20px;line-height:24px;
    transform-origin:left top;transform:rotate(-90deg);
  }
  .spine-author{top:273px;letter-spacing:.5px}
  .spine-title{top:740px}
</style>
</head>
<body>
  <div class="spread">
    <div class="clouds" role="img" aria-label="Soft white clouds beneath a blue sky"></div>

    <section class="panel back">
      <div class="author-photo" role="img" aria-label="Portrait photograph of the author"></div>
      <p class="blurb">
        <strong>Meera Lindqvist Rao</strong><br>
        (a university professor) tells her<br>
        story through her own<br>
        Songs and Poems.<br>
        Sharing with the people she loved,<br>
        especially her grand children, her<br>
        extensive professional and life<br>
        interests, her family, friends, and<br>
        festivities, her illness.
      </p>
      <p class="book-title book-title-back">
        <span>Quiet Verses</span>
        <span>Across</span>
        <span>Winter Evenings</span>
      </p>
    </section>

    <section class="panel spine">
      <span class="spine-text spine-author">Meera Lindqvist Rao</span>
      <span class="spine-text spine-title">Quiet Verses Across Winter Evenings</span>
    </section>

    <section class="panel front">
      <h2 class="front-author">Meera Lindqvist Rao</h2>
      <h1 class="book-title book-title-front">
        <span>Quiet Verses</span>
        <span>Across</span>
        <span>Winter Evenings</span>
      </h1>
    </section>
  </div>
</body>
</html>
```